Corinne Hale

I need a label design for a Woman's Professional Haircare line sold to salons. So the label would be on Shampoo's, Conditioners , serum's, styling products, bleaches, etc...
I'm looking at a softer color label design like lavender or shades of lighter purple. i would like Logo to be or contain a Petalune. Here are a few designs from the professional ranks that are different. They use the solid colors with the back design. I was thinking something like this might work.

Colors
A7469A
B969AE
D3A5CF
EDDBEB
F8F0F9
6B429C
8869AF
B7A5CE
E3DAEB
F3F0F8

```html
<!DOCTYPE html>
<html lang="en">
<head>
<meta charset="utf-8">
<title>Petalune Professional Haircare Labels</title>
<link rel="stylesheet" href="https://fonts.googleapis.com/css2?family=Nunito+Sans:wght@300;700&display=swap">
<style>
  :root {
    --canvas: #f1eeea;
    --ink: #ffffff;
    --lavender-deep: #8869af;
    --lavender-mid: #a58bc8;
    --lavender-soft: #b7a5ce;
    --orchid-deep: #a7469a;
    --orchid-mid: #c27ab7;
    --orchid-soft: #d3a5cf;
    --violet-deep: #8a4fa6;
    --violet-mid: #a866b3;
    --violet-soft: #c48ac8;
    --rule: rgba(255, 255, 255, 0.75);
  }
  * { margin: 0; padding: 0; box-sizing: border-box; }
  html, body {
    width: 1200px;
    height: 988px;
    overflow: hidden;
    background: var(--canvas);
  }
  .label-range {
    position: relative;
    width: 1200px;
    height: 988px;
    display: flex;
    justify-content: center;
    align-items: flex-end;
    gap: 36px;
    padding-bottom: 120px;
  }
  .label {
    position: relative;
    width: 300px;
    border-radius: 10px;
    overflow: hidden;
    color: var(--ink);
    font-family: "Nunito Sans", sans-serif;
    font-weight: 300;
    text-align: center;
  }
  .label--spray { height: 560px; }
  .label--pump { height: 700px; }
  .label--bottle { height: 700px; }
  .label__pattern {
    position: absolute;
    inset: 0;
  }
  .label--spray .label__pattern {
    background: linear-gradient(100deg, var(--lavender-deep) 0%, var(--lavender-mid) 55%, var(--lavender-soft) 100%);
  }
  .label--pump .label__pattern {
    background: linear-gradient(100deg, var(--orchid-deep) 0%, var(--orchid-mid) 55%, var(--orchid-soft) 100%);
  }
  .label--bottle .label__pattern {
    background: linear-gradient(100deg, var(--violet-deep) 0%, var(--violet-mid) 55%, var(--violet-soft) 100%);
  }
  .label__content {
    position: relative;
    height: 100%;
    display: flex;
    flex-direction: column;
    align-items: center;
    padding: 0 24px;
  }
  .brand {
    font-size: 34px;
    letter-spacing: 1px;
    line-height: 1;
  }
  .label--spray .brand { margin-top: 110px; }
  .label--pump .brand { margin-top: 150px; }
  .label--bottle .brand { margin-top: 130px; }
  .product__line {
    font-weight: 700;
    font-size: 19px;
    line-height: 1.2;
  }
  .product__name,
  .product__detail {
    font-size: 20px;
    line-height: 1.3;
  }
  .label--spray .product__line { margin-top: 150px; }
  .label--pump .product__line { margin-top: 190px; }
  .label--bottle .product__name { margin-top: 260px; }
  .product__name { margin-top: 10px; }
  .rule {
    width: 96px;
    height: 1px;
    background: var(--rule);
    margin: 14px 0 14px;
  }
</style>
</head>
<body>
  <main class="label-range">
    <article class="label label--spray">
      <div class="label__pattern" role="img" aria-label="Lavender faceted triangle pattern background"></div>
      <div class="label__content">
        <p class="brand">Petalune</p>
        <p class="product__line">3D</p>
        <p class="product__name">color-lock<br>conditioner</p>
        <span class="rule"></span>
        <p class="product__detail">volume one enhancing<br>shampoo</p>
      </div>
    </article>

    <article class="label label--pump">
      <div class="label__pattern" role="img" aria-label="Orchid pink faceted triangle pattern background"></div>
      <div class="label__content">
        <p class="brand">Petalune</p>
        <p class="product__line">vault</p>
        <p class="product__name">color-lock<br>conditioner</p>
        <span class="rule"></span>
        <p class="product__detail">conditioner blond<br>hair polar</p>
      </div>
    </article>

    <article class="label label--bottle">
      <div class="label__pattern" role="img" aria-label="Violet faceted triangle pattern background"></div>
      <div class="label__content">
        <p class="brand">Petalune</p>
        <p class="product__name">Cool blonde<br>shampoo</p>
        <span class="rule"></span>
        <p class="product__detail">Shampoo Blond<br>hair polar</p>
      </div>
    </article>
  </main>
</body>
</html>
```